Quote Cards With TK May 2025 for Instagram

I would like to put these quotes over one of the pictures attached; Instagram (new size: 4:5 (1080 x 1350 pixels) One Quote per picture, and I want the quote to be bold or easy to read as well. I provided a few reference graphics that I really like as examples below. In very small letters at the bottom add @TKBarlowOnline

All of the pictures are attached; you can pick any photo and add one quote to it; but no stock photography

```html
<!DOCTYPE html>
<html lang="en">
<head>
<meta charset="UTF-8">
<title>Quote Card – TK</title>
<link rel="stylesheet" href="https://fonts.googleapis.com/css2?family=Marcellus&family=Poppins:wght@600&display=swap">
<style>
  :root {
    --pink: #ff3ba2;
    --photo-light: #d9d2d4;
    --photo-mid: #a8949c;
    --photo-dark: #3a2a33;
    --white: #ffffff;
  }
  html, body {
    margin: 0;
    padding: 0;
    overflow: hidden;
    background: var(--white);
  }
  .card {
    position: relative;
    width: 960px;
    height: 1200px;
    overflow: hidden;
    background: var(--pink);
  }
  .card__photo {
    position: absolute;
    inset: 0;
    background:
      radial-gradient(ellipse 260px 520px at 300px 760px, var(--photo-dark) 0%, rgba(58,42,51,0.6) 45%, rgba(58,42,51,0) 100%),
      linear-gradient(180deg, var(--photo-light) 0%, #c9bec3 55%, var(--photo-mid) 100%);
  }
  .card__tint {
    position: absolute;
    inset: 0;
    background: linear-gradient(90deg,
      rgba(255,59,162,0) 0%,
      rgba(255,59,162,0.15) 25%,
      rgba(255,59,162,0.55) 48%,
      rgba(255,59,162,0.9) 62%,
      var(--pink) 75%);
  }
  .card__frame {
    position: absolute;
    inset: 0;
  }
  .quote {
    position: absolute;
    left: 412px;
    width: 500px;
    top: 272px;
    margin: 0;
    font-family: "Marcellus", serif;
    font-size: 64px;
    line-height: 75px;
    color: var(--white);
    text-align: center;
    font-weight: 400;
    -webkit-text-stroke: 1.8px var(--white);
    paint-order: stroke fill;
  }
  .quote__line { display: block; white-space: nowrap; }
  .quote__closer { display: block; margin-top: 64px; }
  .handle {
    position: absolute;
    left: 0;
    width: 960px;
    top: 1124px;
    text-align: center;
    font-family: "Poppins", sans-serif;
    font-weight: 600;
    font-size: 31px;
    line-height: 40px;
    color: var(--white);
  }
</style>
</head>
<body>
  <main class="card">
    <div class="card__photo" role="img" aria-label="Photo of TK in a white cropped sweater and dark leggings, posing in a bright kitchen"></div>
    <div class="card__tint"></div>

    <svg class="card__frame" width="960" height="1200" viewBox="0 0 960 1200" aria-hidden="true">
      <path d="M 315 1145 L 70 1145 Q 34 1145 34 1109 L 34 76 Q 34 40 70 40 L 892 40 Q 928 40 928 76 L 928 1109 Q 928 1145 892 1145 L 645 1145"
            fill="none" stroke="#ffffff" stroke-width="3" stroke-linecap="round"/>
    </svg>

    <p class="quote">
      <span class="quote__line">Bloating.</span>
      <span class="quote__line">Muffin top.</span>
      <span class="quote__line">Puffy waistline.</span>
      <span class="quote__line">Your body’s</span>
      <span class="quote__line">screaming</span>
      <span class="quote__line">for a different</span>
      <span class="quote__line">kind of fix.</span>
      <span class="quote__closer">Here it is</span>
    </p>

    <div class="handle">@TKBarlowOnline</div>
  </main>
</body>
</html>
```